Rise As Captain Book Cover Design

Book Cover Design Brief
Book Title
Rise As Captain
Subtitle
The 10 Quiet Habits of Remarkable Command
Author
Orwen Dalquist
Overview
This book is about leadership that starts within.
Most leadership books focus on tactics or management strategies. This book focuses on the inner disciplines that create powerful leaders — mindset, integrity, focus, empathy, professionalism, honesty, and self-respect.
The tone of the book is bold, direct, confident, and transformational.
This is not a soft or corporate leadership book. It is a call to step up and become the leader you are capable of becoming.
The cover should feel:
• Powerful
• Professional
• Transformational
• Premium
• Memorable
Think best-selling leadership book, not a generic business book.
Target Audience
Business owners
Managers
Entrepreneurs
Team leaders
Professionals who want to grow as leaders
Most readers are ambitious professionals who want to level up their leadership and life.
Design Direction
The design should communicate:
Strength. Discipline. Leadership. Personal transformation.
Avoid cliché leadership visuals like:
• Handshakes
• Office buildings
• Corporate stock imagery
• Teams sitting around tables
The design should feel iconic, bold, and timeless.
Think about covers of successful leadership books such as:
Copper Rituals
Total Stewardship
Won't Break Now
Begin From Purpose
The 36 Rules of Sway
These covers are simple, powerful, and recognizable even at small sizes.
Typography
The title RISE AS CAPTAIN should be:
• Bold
• Strong
• Dominant on the cover
• Easy to read even at small sizes (important for Vellora thumbnails)
The subtitle should be clean and secondary to the title.
The overall typography should feel strong, modern, and premium.
Color Direction
Designers are free to explore colors, but the cover should feel strong and premium, not playful.
Colors that often work well for leadership books include:
Black
Gold
White
Deep blue
Dark red
High contrast and clarity are important.
Style
Preferred style:
• Clean
• Modern
• Minimal
• Strong contrast
Avoid clutter and overly busy designs.
The goal is to create a cover that feels powerful and professional at first glance.
Deliverables
Front cover design for a leadership book.
Final files should include:
• High resolution artwork
• Editable source files
• Print-ready version suitable for publishing
Goal of the Cover
When someone sees this book on Vellora or in a bookstore, they should immediately think:
“This looks like a serious leadership book.”
The design should feel like it belongs next to books by authors such as:
Marcus Thorley
Brandt Osgood
Peter Hollis
Nolan Fairbrook
A strong, confident cover that attracts leaders who want to grow and perform at a higher level.
Target Market(s)
Business Owners and High level managers
Look and feel
Each slider illustrates characteristics of the customer's brand and the style your logo design should communicate.

```html
<!DOCTYPE html>
<html lang="en">
<head>
<meta charset="utf-8">
<title>Rise As Captain — Book Cover</title>
<link rel="stylesheet" href="https://fonts.googleapis.com/css2?family=Bebas+Neue&family=Arimo:wght@700&family=Open+Sans:wght@400&display=swap">
<style>
  :root {
    --cover-black: #040606;
    --gold-deep: #d6972a;
    --gold-mid: #ecb93f;
    --gold-light: #fcdc74;
    --text-white: #ffffff;
  }
  html, body {
    margin: 0;
    padding: 0;
    width: 849px;
    height: 1200px;
    overflow: hidden;
    background: var(--cover-black);
  }
  .cover {
    position: relative;
    width: 849px;
    height: 1200px;
    background: var(--cover-black);
  }
  .cover-art {
    position: absolute;
    inset: 0;
    width: 849px;
    height: 1200px;
  }
  .author-name {
    font-family: "Arimo", Arial, sans-serif;
    font-weight: 700;
    font-size: 34px;
    letter-spacing: 10px;
  }
  .title-line {
    font-family: "Bebas Neue", "Oswald", sans-serif;
  }
  .subtitle {
    position: absolute;
    left: 0;
    right: 0;
    top: 834px;
    margin: 0;
    text-align: center;
    font-family: "Open Sans", Calibri, sans-serif;
    font-weight: 400;
    font-size: 30px;
    line-height: 45px;
    color: var(--text-white);
  }
</style>
</head>
<body>
<main class="cover">
  <svg class="cover-art" viewBox="0 0 849 1200" xmlns="http://www.w3.org/2000/svg">
    <defs>
      <linearGradient id="gold-sheen" gradientUnits="userSpaceOnUse" x1="520" y1="170" x2="330" y2="760">
        <stop offset="0" stop-color="var(--gold-light)"/>
        <stop offset="0.18" stop-color="var(--gold-deep)"/>
        <stop offset="0.45" stop-color="var(--gold-light)"/>
        <stop offset="0.7" stop-color="var(--gold-mid)"/>
        <stop offset="1" stop-color="var(--gold-light)"/>
      </linearGradient>
      <linearGradient id="rule-gold" x1="0" y1="0" x2="1" y2="0">
        <stop offset="0" stop-color="var(--gold-light)" stop-opacity="0.6"/>
        <stop offset="0.5" stop-color="var(--gold-deep)"/>
        <stop offset="1" stop-color="var(--gold-light)" stop-opacity="0.6"/>
      </linearGradient>
    </defs>

    <text class="author-name" x="424.5" y="78" text-anchor="middle" fill="var(--gold-mid)">ORWEN DALQUIST</text>

    <g class="title" fill="url(#gold-sheen)" text-anchor="middle">
      <text class="title-line title-line--rise" x="424.5" y="388" font-size="299" textLength="430" lengthAdjust="spacingAndGlyphs">RISE</text>
      <text class="title-line title-line--as" x="424.5" y="550" font-size="203" textLength="150" lengthAdjust="spacingAndGlyphs">AS</text>
      <text class="title-line title-line--captain" x="424.5" y="743" font-size="230" textLength="560" lengthAdjust="spacingAndGlyphs">CAPTAIN</text>
    </g>

    <polygon class="rule rule--top" points="132,820 434,817.5 736,820 434,822.5" fill="url(#rule-gold)"/>
    <polygon class="rule rule--bottom" points="132,945 434,942.5 736,945 434,947.5" fill="url(#rule-gold)"/>
  </svg>

  <p class="subtitle">The 10 Quiet Habits of<br>Remarkable Command</p>
</main>
</body>
</html>
```